Business Card Design for Brightkeel

The company provides engineering tender consulting services and personnel resources. The target market is large engineering construction and services companies. The business is based in Australia.

```html
<!DOCTYPE html>
<html lang="en">
<head>
<meta charset="utf-8">
<title>Brightkeel Business Card</title>
<link rel="stylesheet" href="https://fonts.googleapis.com/css2?family=Open+Sans:wght@400;600;700&display=swap">
<style>
  :root {
    --page-bg: #ececec;
    --brand-blue: #1a9be6;
    --band-blue-dark: #1478b8;
    --band-blue-light: #5cc0f2;
    --card-dark-top: #2a2a2a;
    --card-dark-bottom: #0c0c0c;
    --card-light-top: #f4f4f4;
    --card-light-bottom: #c9c9c9;
    --ink-dark: #222222;
    --ink-mid: #555555;
    --ink-light: #e6e6e6;
    --ink-muted: #b5b5b5;
  }
  * { box-sizing: border-box; margin: 0; padding: 0; }
  html, body { width: 855px; height: 1200px; overflow: hidden; }
  body {
    background: var(--page-bg);
    font-family: "Open Sans", Arial, sans-serif;
    position: relative;
  }
  .card {
    position: absolute;
    left: 77px;
    width: 700px;
    height: 400px;
    overflow: hidden;
    box-shadow: 0 6px 18px rgba(0,0,0,0.25);
  }
  .card--back { top: 150px; background: linear-gradient(180deg, var(--card-dark-top), var(--card-dark-bottom)); color: var(--ink-light); }
  .card--front { top: 650px; background: linear-gradient(180deg, var(--card-light-top), var(--card-light-bottom)); color: var(--ink-dark); }
  .card__band {
    position: absolute; top: 0; left: 0; right: 0; height: 22px;
    background: linear-gradient(90deg, var(--band-blue-dark) 0%, var(--brand-blue) 35%, var(--band-blue-light) 65%, var(--brand-blue) 100%);
  }
  .card__chevrons { position: absolute; left: 0; bottom: 0; }
  .card__watermark {
    position: absolute; left: 30px; font-weight: 700; font-size: 92px;
    letter-spacing: -2px; white-space: nowrap;
  }
  .card--back .card__watermark { top: 118px; color: rgba(255,255,255,0.07); }
  .card--front .card__watermark { top: 50px; color: rgba(255,255,255,0.55); }

  .about {
    position: absolute; top: 36px; left: 26px; right: 26px;
    font-size: 11.5px; line-height: 1.3; color: var(--ink-light);
  }
  .about__name { color: var(--brand-blue); }
  .services {
    position: absolute; left: 170px; top: 240px; width: 500px; height: 140px;
    color: var(--ink-light);
  }
  .services span { position: absolute; white-space: nowrap; }

  .identity { position: absolute; right: 30px; top: 32px; text-align: right; }
  .identity__name { font-size: 20px; color: var(--ink-dark); }
  .identity__role { font-size: 11px; color: var(--ink-mid); }
  .logo-strip {
    position: absolute; left: 0; top: 108px; width: 430px; height: 74px;
    background: linear-gradient(90deg, rgba(255,255,255,0.95) 60%, rgba(255,255,255,0));
  }
  .logo {
    position: absolute; left: 24px; top: 120px;
    font-size: 50px; font-weight: 600; color: var(--brand-blue); letter-spacing: -1px;
  }
  .contact {
    position: absolute; right: 30px; top: 220px; text-align: right;
    font-size: 13.5px; line-height: 1.55; color: var(--ink-dark);
  }
  .contact__company { font-size: 24px; font-weight: 700; line-height: 1.3; }
</style>
</head>
<body>

  <section class="card card--back" aria-label="Business card back">
    <div class="card__band"></div>
    <svg class="card__chevrons" width="360" height="240" viewBox="0 0 360 240" aria-hidden="true">
      <polygon points="0,0 130,120 0,240" fill="#3a3a3a"/>
      <polygon points="0,30 100,120 0,210" fill="#474747"/>
      <polygon points="0,60 70,120 0,180" fill="#555555"/>
      <polygon points="0,240 130,120 170,240" fill="#2c2c2c"/>
    </svg>
    <div class="card__watermark">Brightkeel</div>
    <p class="about"><span class="about__name">Brightkeel</span> provides engineering tender consulting services and personnel resources. With a experience of more than a decade in strategy, business process and change management, business process outsourcing, marketing, sales, business development, and technology with hands-on, integrated implementation. Unlike traditional consulting firms, we combine real world analysis and global problem solving experience with actual implementational resources focused on helping businesses and organizations grow and expand as well as operate more effectively and profitably.</p>
    <div class="services">
      <span style="left:0;top:0;font-size:14px;">Project Management</span>
      <span style="left:150px;top:-2px;font-size:17px;">Logical &amp; Creative Thinking</span>
      <span style="left:10px;top:20px;font-size:20px;">Strategic Planning</span>
      <span style="left:195px;top:26px;font-size:14px;">Value Management</span>
      <span style="left:60px;top:48px;font-size:23px;">Bid Management and Strategy</span>
      <span style="left:20px;top:80px;font-size:13px;">Independent estimations</span>
      <span style="left:230px;top:76px;font-size:13px;">Risk Management</span>
      <span style="left:140px;top:96px;font-size:14px;">Independent estimations</span>
      <span style="left:45px;top:117px;font-size:13px;">Total asset Management</span>
      <span style="left:260px;top:113px;font-size:17px;">Cost Management</span>
    </div>
  </section>

  <section class="card card--front" aria-label="Business card front">
    <div class="card__band"></div>
    <svg class="card__chevrons" width="340" height="220" viewBox="0 0 340 220" aria-hidden="true">
      <polygon points="0,0 130,110 0,220" fill="#dcdcdc"/>
      <polygon points="0,30 95,110 0,190" fill="#cfcfcf"/>
      <polygon points="0,60 60,110 0,160" fill="#bdbdbd"/>
      <polygon points="0,220 130,110 170,220" fill="#e4e4e4"/>
    </svg>
    <div class="card__watermark">Brightkeel</div>
    <div class="identity">
      <p class="identity__name">Firstname Surname</p>
      <p class="identity__role">Designation</p>
    </div>
    <div class="logo-strip"></div>
    <p class="logo">Brightkeel</p>
    <div class="contact">
      <p class="contact__company">Brightkeel</p>
      <p>PO Box 99 Nnnnnnnnnn, Nnn, 9999</p>
      <p>ABN 9999999999</p>
      <p>M: 9999 999 999</p>
      <p>T: 99 9999 9999</p>
      <p>E: nnnn@nnn.com.au</p>
    </div>
  </section>

</body>
</html>
```